Book cover design for a collection of poetry - The Lanternfield

Book cover and back design need to be moody, nostalgic, reflective, ethereal. Melancholy and other worldly. Cover design should not be time specific to a period or place but if applicable should reflect British landscape. Book cover should be in tones of blue and must include the title and author (THE LANTERNFIELD BY DORIAN WELKBRIDGE). We love the idea of rain, and looking out of a window. See attached designs. A world you are observing but not in.

Industry/Entity Type

Book Publisher

Font styles to use
Serif
Script

Colors
3176b5
3377b5
85acd3
eaf1f7
0792cd
33a6d7
86cae7
ecf7fb
86cfc6

Requirements
Must have
• The colour blue in it, must be melancholy and reflective.
Nice to have
• Rain in the cover.
Should not have
• Any bright colours.

```html
<!DOCTYPE html>
<html lang="en">
<head>
<meta charset="utf-8">
<title>The Lanternfield — Dorian Welkbridge</title>
<link rel="stylesheet" href="https://fonts.googleapis.com/css2?family=Playfair+Display:wght@400&family=Cinzel:wght@500&display=swap">
<style>
  :root {
    --ink-dark: #111915;
    --ink-deep: #1c2824;
    --glass-light: #e4eff2;
    --glass-mist: #a9c8d2;
    --rain-blue: #5f8fa6;
    --title-teal: #74a9bb;
    --author-white: #f4f6f7;
  }
  * { margin: 0; padding: 0; box-sizing: border-box; }
  html, body {
    width: 750px;
    height: 1200px;
    overflow: hidden;
    background: var(--ink-dark);
  }
  .cover {
    position: relative;
    width: 750px;
    height: 1200px;
    overflow: hidden;
    background: var(--ink-dark);
  }
  .cover-scene {
    position: absolute;
    inset: 0;
    background:
      radial-gradient(ellipse 210px 330px at 340px 300px, var(--glass-light) 0%, var(--glass-mist) 45%, rgba(95,143,166,0.55) 75%, rgba(28,40,36,0) 100%),
      radial-gradient(ellipse 230px 260px at 340px 700px, var(--rain-blue) 0%, rgba(66,104,122,0.7) 50%, rgba(28,40,36,0) 100%),
      radial-gradient(ellipse 420px 620px at 360px 460px, var(--ink-deep) 0%, var(--ink-dark) 100%);
  }
  .title {
    font-family: "Playfair Display", serif;
    font-weight: 400;
    color: var(--title-teal);
    line-height: 1;
  }
  .title-article,
  .title-main {
    position: absolute;
    display: block;
    white-space: nowrap;
  }
  .title-article {
    left: 214px;
    top: 928px;
    font-size: 76px;
    letter-spacing: -1px;
  }
  .title-main {
    left: 102px;
    top: 976px;
    font-size: 104px;
    letter-spacing: -3px;
  }
  .author {
    position: absolute;
    right: 115px;
    top: 1100px;
    font-family: "Cinzel", serif;
    font-weight: 500;
    font-size: 24px;
    line-height: 1;
    letter-spacing: 0.5px;
    color: var(--author-white);
    white-space: nowrap;
  }
</style>
</head>
<body>
  <main class="cover">
    <div class="cover-scene" role="img" aria-label="Photograph of a rain-streaked four-pane window in a dark room, a sheer blue curtain drawn to one side and a misty blue landscape beyond the glass"></div>
    <h1 class="title">
      <span class="title-article">the</span>
      <span class="title-main">lanternfield</span>
    </h1>
    <p class="author">DORIAN WELKBRIDGE</p>
  </main>
</body>
</html>
```